PDF to help promote my website to potential advertisers

I need a one page PDF that may be used on our site to help promote my website (LKPhomes.com) to potential advertisers. It's a pretty simple document but needs to make it look great.

I've provided the audience info. I'm hoping to have this look sorta like the Market Ledger's advertising page: http://www.marketledger-example.com/advertise

It's not rocket science but I hope you can help.

Target Market(s)

Potential Advertisers are typically home improvement-related-services like contractors and home builders. Also real estate agents and home-sales related services.

Industry/Entity Type

Media

Colors

Designer to choose colors to be used in the design.

Requirements
Must have
• I want the graphics to make the audience info (in the txt file) stand out. Needs to be similar to this: http://www.marketledger-example.com/advertise.
• I want to use the PDF to send via email to prospective clients and also post on our website, so it has to be able to work almost like graphics on a site. I may have it printed as well.
Nice to have
• Colors and logo and font should match our site. Please grab the logo and/font info from our site

```html
<!DOCTYPE html>
<html lang="en">
<head>
<meta charset="utf-8">
<title>Advertising with LKPhomes</title>
<link href="https://fonts.googleapis.com/css2?family=Exo+2:wght@300;400;600;700;800&display=swap" rel="stylesheet">
<style>
  :root {
    --ink-dark: #1c1d1f;
    --ink-deep: #121314;
    --brand-blue: #1ea3e4;
    --panel-teal: #1c6283;
    --stone-grey: #a9abad;
    --soft-grey: #8d8f92;
    --paper: #ffffff;
    --body-text: #3d4247;
    --rule-grey: #cfd3d6;
  }
  * { margin: 0; padding: 0; box-sizing: border-box; }
  html, body { width: 998px; height: 1200px; overflow: hidden; background: var(--ink-deep); }
  body { font-family: "Exo 2", sans-serif; }
  .poster { position: relative; width: 998px; height: 1200px; overflow: hidden; background: var(--ink-dark); }
  .backdrop-photo {
    position: absolute; left: 0; right: 0; top: 0; height: 930px;
    background: linear-gradient(180deg, #2a2b2d 0%, #222325 50%, #232624 100%);
  }
  .house-photo {
    position: absolute; left: 80px; right: 0; top: 480px; height: 450px;
    background: linear-gradient(180deg, #6e4a3c 0%, #a98a72 45%, #c9bda3 75%, #5a5646 100%);
  }
  .masthead { position: absolute; top: 48px; left: 0; right: 0; text-align: center; }
  .brand-row { display: inline-flex; align-items: center; gap: 20px; }
  .brand-mark { width: 70px; height: 60px; background: var(--brand-blue); }
  .brand-name { font-size: 62px; font-weight: 600; color: var(--stone-grey); letter-spacing: 1px; line-height: 1; }
  .tagline { margin-top: 8px; font-size: 21px; color: var(--soft-grey); }
  .headline { position: absolute; top: 182px; left: 0; right: 0; text-align: center; line-height: 0.98; }
  .headline-main { font-size: 90px; font-weight: 800; color: var(--brand-blue); letter-spacing: 1px; }
  .headline-sub { font-size: 78px; font-weight: 400; color: var(--brand-blue); }
  .headline-sub .brand-word { font-weight: 600; color: var(--stone-grey); }
  .pitch { position: absolute; top: 352px; left: 0; right: 0; text-align: center; color: var(--paper); line-height: 1.25; }
  .pitch-lead { font-size: 31px; font-weight: 400; }
  .pitch-focus { font-size: 36px; font-weight: 800; }
  .pitch-tail { font-size: 28px; font-weight: 400; }
  .about-panel { position: absolute; left: 0; right: 0; top: 930px; bottom: 0; background: var(--paper); }
  .about-tab {
    position: absolute; top: -22px; left: 0; height: 44px; padding: 0 70px 0 58px;
    background: var(--panel-teal); color: var(--paper); font-size: 20px; font-weight: 700;
    display: flex; align-items: center;
    clip-path: polygon(0 0, 88% 0, 100% 100%, 0 100%);
  }
  .about-rule { position: absolute; top: 18px; left: 0; right: 0; height: 4px; background: var(--panel-teal); }
  .reach-line { position: absolute; top: 40px; left: 58px; right: 40px; font-size: 15.5px; color: var(--body-text); white-space: nowrap; }
  .stat-columns { position: absolute; top: 76px; left: 58px; right: 40px; display: flex; }
  .stat-list { list-style: none; flex: 1; }
  .stat-list + .stat-list { border-left: 1px solid var(--rule-grey); padding-left: 24px; }
  .stat-list li { font-size: 15px; color: var(--body-text); margin-bottom: 10px; white-space: nowrap; }
  .stat-figure { font-weight: 700; color: var(--panel-teal); margin-right: 7px; }
  .footer-band {
    position: absolute; left: 0; right: 0; bottom: 12px; height: 66px; background: var(--panel-teal);
    display: flex; align-items: center; justify-content: center; gap: 20px;
  }
  .site-url { color: var(--paper); font-size: 18px; letter-spacing: 12px; text-transform: uppercase; }
  .social-square { width: 22px; height: 22px; background: var(--paper); border-radius: 4px; }
</style>
</head>
<body>
<main class="poster">
  <div class="backdrop-photo" role="img" aria-label="Darkened photo of a white house facade with porch and trees"></div>
  <div class="house-photo" role="img" aria-label="Photo of a cream stucco house with red tiled roof and brick chimney"></div>

  <header class="masthead">
    <div class="brand-row">
      <span class="brand-mark"></span>
      <span class="brand-name">LKPHOMES</span>
    </div>
    <p class="tagline">Obsessed with great homes around Milwaukee</p>
  </header>

  <h1 class="headline">
    <span class="headline-main">ADVERTISING</span><br>
    <span class="headline-sub">with <span class="brand-word">LKPHOMES</span></span>
  </h1>

  <section class="pitch">
    <p class="pitch-lead">Learn how you can partner with us to reach</p>
    <p class="pitch-focus">OUR MILWAUKEE AUDIENCE</p>
    <p class="pitch-tail">who desire to move and/or renovate their homes</p>
  </section>

  <section class="about-panel">
    <div class="about-rule"></div>
    <h2 class="about-tab">About LKPhomes.com</h2>
    <p class="reach-line">We reach over 1000 readers each day through our website, our Linkbook Page, our Snapgram and our email newsletter.</p>
    <div class="stat-columns">
      <ul class="stat-list">
        <li><span class="stat-figure">67%</span>are women</li>
        <li><span class="stat-figure">55%</span>in the prime home purchase age range of 25-44</li>
        <li><span class="stat-figure">75%</span>in milwaukee area</li>
      </ul>
      <ul class="stat-list">
        <li><span class="stat-figure">60%</span>claim they are "happy but looking" for a future new home</li>
        <li><span class="stat-figure">55%</span>plan to do a home improvement projects in the next year</li>
        <li><span class="stat-figure">30%</span>do not have an agent</li>
      </ul>
    </div>
    <footer class="footer-band">
      <span class="site-url">www.lkphomes.com</span>
      <span class="social-square"></span>
      <span class="social-square"></span>
    </footer>
  </section>
</main>
</body>
</html>
```